Velvora Beauty Sensitive Skin Intimate Shave Cream

We need a label/package design for a female shave cream. Our brand is Velvora Beauty and we manufacturer luxuriously sexy female intimate items. We are looking for sexy packaging to really get our brand out there. I have included in attachments, all of the files including font, logo, size requirements and verbage requirements. On the file "shave-cream-requirements" please use to format for size. Also on that file, I need the "must have" verbage from my project brief laid out exactly the same. The name of the product is Velvora Beauty Classic Silken Intimate Shave Cream
Target Market(s)
Females who like luxury and feeling sexy
Industry/Entity Type
Manufacturer
Requirements
Must have
- Must have my velvora beauty logo. The scent for this cream is called "silken classic" Please put that one the label. Also the actual scent is "an array of light florals with a hint of baby powder" please put that in small letters on back of the label
- Must be Label Dimensions: 6.25h X 7.375w
- Must say "Intimate Shave Cream for Her".
- Must say - Fill Weight: 16 Fl. Oz. (480ml) ℮
- must say - Suggested use: Apply intimate shave cream where desired and glide razor over skin for smooth results
- Must say - Ingredient Deck:
- Water (Eau/Aqua), Cetyl Alcohol, Cetrimonium Bromide, Stearyl Alcohol, Hydroxyethylcellulose, Glyceryl Stearate, PEG-100 Stearate, PEG-60 Lanolin, Simmondsia Chinensis (Jojoba) Seed Oil, Hydrolyzed Keratin, Panthenol, Allantoin, Phenoxyethanol, Methylisothiazolinone, Sodium Hydroxide, Fragrance (Parfum)
- Must say these cautions:
- Recommend Cautions:
- Do Not Use if You have a Known Hypersensitivity (Allergy) to Any of the Ingredients
- If Irritation Occurs, Discontinue Use
- If Eye Contact Occurs, Rinse with Water to Remove
- Keep Out of Reach of Children
- Must say : Specially formulated with skin soothing ingredients to provide a smooth and effortless shave.
- Protects and nourishes from irritation and razor cuts
- Helps prevent embarrassing shave rashes and ingrown hairs.
- Designed for sensitive and intimate skin. Perfect for intimate areas, legs, underarms, face, and body.
- Enhanced with hair and skin moisturizing agents.
- Can also be used to condition skin and hair after shampoo.
- Must have UPC (included) and part number:VK584731 in small writing on the back of the label.
Should not have
- cheap looking designs and logos

```html
<!DOCTYPE html>
<html lang="en">
<head>
<meta charset="utf-8">
<title>Velvora Beauty Classic Silken Intimate Shave Cream – Label</title>
<link href="https://fonts.googleapis.com/css2?family=Great+Vibes&family=Josefin+Sans:wght@300;400;600&display=swap" rel="stylesheet">
<style>
  :root {
    --page: #ffffff;
    --label-top: #1e0019;
    --label-bottom: #7a0132;
    --stripe-top: #5c0b57;
    --stripe-bottom: #ac1271;
    --ink: #ffffff;
    --ink-soft: #e9dbe4;
    --shadow: rgba(0,0,0,0.12);
  }
  * { margin: 0; padding: 0; box-sizing: border-box; }
  html, body { width: 1200px; height: 1017px; overflow: hidden; background: var(--page); }
  body { position: relative; font-family: "Josefin Sans", sans-serif; color: var(--ink); }

  .sheet-edge {
    position: absolute; left: 0; top: 78px; width: 1200px; height: 856px;
    background: var(--page); box-shadow: 0 0 14px var(--shadow);
  }
  .label {
    position: absolute; left: 119px; top: 101px; width: 963px; height: 815px;
    background: linear-gradient(to bottom, var(--label-top), var(--label-bottom));
  }
  .stripe {
    position: absolute; top: 0; height: 100%;
    background: linear-gradient(to bottom, var(--stripe-top), var(--stripe-bottom));
  }
  .stripe--left { left: 287px; width: 53px; }
  .stripe--right { left: 627px; width: 49px; }

  .abs { position: absolute; }

  /* back panel */
  .back-panel { left: 14px; width: 254px; font-size: 10px; font-weight: 300; line-height: 21.7px; color: var(--ink-soft); }
  .back-panel p { text-align: justify; text-align-last: left; }
  .back-heading { font-weight: 600; color: var(--ink); }
  .underlined { text-decoration: underline; }
  .claim { font-weight: 600; color: var(--ink); text-decoration: underline; text-align: center !important; text-align-last: center !important; }

  /* front panel */
  .front { left: 340px; width: 287px; text-align: center; }
  .scent-name { font-family: "Great Vibes", cursive; line-height: 1; }
  .scent-name--top { top: 28px; font-size: 74px; }
  .scent-name--bottom { top: 128px; font-size: 84px; }
  .from { top: 252px; font-size: 20px; font-weight: 300; }
  .wordmark { font-weight: 300; letter-spacing: 0.42em; text-indent: 0.42em; line-height: 1; }
  .wordmark-sub { font-weight: 300; letter-spacing: 0.5em; text-indent: 0.5em; font-size: 11px; line-height: 1; }
  .front-mark { top: 303px; font-size: 34px; }
  .front-mark-sub { top: 345px; }
  .product-line { font-weight: 300; font-variant: small-caps; line-height: 1; white-space: nowrap; }
  .product-line--intimate { top: 464px; font-size: 50px; letter-spacing: 0.22em; text-indent: 0.22em; }
  .product-line--cream { top: 530px; font-size: 50px; letter-spacing: 0.03em; }
  .for-her { top: 615px; font-size: 20px; font-weight: 300; }
  .fill-weight { top: 770px; font-size: 13px; font-weight: 300; color: var(--ink-soft); }

  /* side panel */
  .side { left: 676px; width: 287px; text-align: center; }
  .scent-notes { top: 50px; font-size: 15px; font-weight: 300; letter-spacing: 0.06em; line-height: 33px; text-transform: uppercase; }
  .side-mark { top: 614px; font-size: 36px; }
  .side-mark-sub { top: 655px; }
  .part-table { left: 698px; top: 746px; width: 242px; font-size: 15px; font-weight: 300; line-height: 20px; }
  .part-row { display: flex; justify-content: space-between; }
</style>
</head>
<body>
  <div class="sheet-edge"></div>

  <main class="label">
    <div class="stripe stripe--left"></div>
    <div class="stripe stripe--right"></div>

    <section class="abs back-panel" style="top:26px;">
      <p class="back-heading">Suggested use:</p>
      <p>Apply intimate shave cream where desired and glide razor over skin for smooth results</p>
    </section>

    <section class="abs back-panel" style="top:123px;">
      <p class="back-heading">Ingredient Deck:</p>
      <p>Water (Eau/Aqua), Cetyl Alcohol, Cetrimonium Bromide, Stearyl Alcohol, Hydroxyethylcellulose, Glyceryl Stearate, PEG-100 Stearate, PEG-60 Lanolin, Simmondsia Chinensis (Jojoba) Seed Oil, Hydrolyzed Keratin, Panthenol, Allantoin, Phenoxyethanol, Methylisothiazolinone, Sodium Hydroxide, Fragrance (Parfum)</p>
    </section>

    <section class="abs back-panel" style="top:320px;">
      <p class="back-heading">Cautions:</p>
      <p class="underlined">Recommend Cautions:</p>
      <p>- Do Not Use if You have a Known Hypersensitivity (Allergy) to Any of the Ingredients?</p>
      <p>- If Irritation Occurs, Discontinue Use?</p>
      <p>- If Eye Contact Occurs, Rinse with Water to Remove?</p>
      <p>- Keep Out of Reach of Children</p>
    </section>

    <section class="abs back-panel" style="top:501px;">
      <p class="claim">Specially formulated with skin soothing ingredients to provide a smooth and effortless shave.</p>
    </section>

    <section class="abs back-panel" style="top:566px;">
      <p>- Protects and nourishes from irritation and razor cuts</p>
      <p>- Helps prevent embarrassing shave rashes and ingrown hairs.</p>
      <p>- Designed for sensitive and intimate skin. Perfect for intimate areas, legs, underarms, face, and body.</p>
      <p>- Enhanced with hair and skin moisturizing agents.</p>
      <p>- Can also be used to condition skin and hair after shampoo.</p>
      <p>- Must have UPC (included) and part number:VK584731 in small writing on the back of the label.</p>
    </section>

    <h1 class="abs front scent-name scent-name--top">Silken</h1>
    <div class="abs front scent-name scent-name--bottom">Classic</div>
    <div class="abs front from">from</div>
    <div class="abs front wordmark front-mark">VELVORA</div>
    <div class="abs front wordmark-sub front-mark-sub">BEAUTY</div>
    <h2 class="abs front product-line product-line--intimate">Intimate</h2>
    <div class="abs front product-line product-line--cream">Shave Cream</div>
    <div class="abs front for-her">For Her</div>
    <div class="abs front fill-weight">Fill Weight: 16 Fl. Oz. (480ml) ℮</div>

    <p class="abs side scent-notes">An array of light florals with a<br>hint of baby powder</p>
    <div class="abs side wordmark side-mark">VELVORA</div>
    <div class="abs side wordmark-sub side-mark-sub">BEAUTY</div>
    <div class="abs part-table">
      <div class="part-row"><span>Model:</span><span>VK584731</span></div>
      <div class="part-row"><span>SKU:</span><span>VK584731</span></div>
    </div>
  </main>
</body>
</html>
```